The name of my company is Tolmen Refacing LLC and I would like the sub text to say "Cabinet Refacing and Countertops". Have my name Dorian Tolmen, Owner / Sales, contact info: Cell: 360-555-0147 / Email: dorian.tolmen@quenmail.com

Simple, Clean, and Organized. With colors that will appeal to the eye.

Target Market(s)

Houses and Apartments

Industry/Entity Type

Cabinet Refacing

Contact Information for Business Card

Company name and sub text Dorian Tolmen - Owner / Sales, my cell phone number and email

Requirements
Must have
• Business name, my name / position, and my contact info
Nice to have
• Simple. Organized. Appealing to the eye

```html
<!DOCTYPE html>
<html lang="en">
<head>
<meta charset="utf-8">
<title>Tolmen Refacing LLC – Business Card</title>
<link href="https://fonts.googleapis.com/css2?family=Jost:wght@300;400;600&display=swap" rel="stylesheet">
<style>
  :root {
    --brand-blue: #3f6fba;
    --ink-gray: #8a8f99;
    --ink-dark: #2b2b2b;
    --card-white: #ffffff;
    --backdrop: #3a3d42;
  }
  html, body {
    margin: 0;
    padding: 0;
    width: 1200px;
    height: 800px;
    overflow: hidden;
    background: var(--backdrop);
    font-family: "Jost", sans-serif;
  }
  .canvas {
    position: relative;
    width: 1200px;
    height: 800px;
  }
  .card {
    position: absolute;
    top: 256px;
    width: 480px;
    height: 289px;
    overflow: hidden;
    box-shadow: 0 6px 14px rgba(0,0,0,0.45);
  }
  .card--front { left: 89px; background: var(--card-white); }
  .card--back { left: 632px; background: var(--brand-blue); }

  .front-corner {
    position: absolute;
    left: 0; top: 0;
  }
  .company-lockup {
    position: absolute;
    left: 210px;
    top: 72px;
    width: 270px;
    text-align: center;
  }
  .company-name {
    margin: 0;
    font-weight: 300;
    font-size: 20px;
    letter-spacing: 0.3px;
    color: var(--ink-gray);
    white-space: nowrap;
  }
  .company-tagline {
    margin: 6px 0 0;
    font-weight: 400;
    font-size: 10px;
    color: var(--ink-dark);
  }
  .person {
    position: absolute;
    left: 52px;
    top: 166px;
  }
  .person-name {
    margin: 0;
    font-size: 22px;
    line-height: 1;
    color: var(--ink-gray);
    font-weight: 300;
  }
  .person-name strong { color: var(--brand-blue); font-weight: 600; }
  .person-role {
    margin: 4px 0 0;
    font-size: 13px;
    font-weight: 300;
    color: var(--ink-gray);
  }
  .contact-list {
    list-style: none;
    margin: 10px 0 0;
    padding: 0;
  }
  .contact-item {
    display: flex;
    align-items: center;
    gap: 5px;
    font-size: 12px;
    font-weight: 300;
    color: var(--ink-gray);
    height: 18px;
  }
  .contact-icon { flex: none; }

  .back-lockup {
    position: absolute;
    left: 118px;
    top: 118px;
    width: 243px;
    text-align: center;
    color: var(--card-white);
  }
  .back-name {
    margin: 0;
    font-size: 25px;
    font-weight: 600;
    line-height: 1;
    letter-spacing: -0.3px;
    white-space: nowrap;
  }
  .back-tagline {
    margin: 5px 0 0;
    padding: 2px 0 3px;
    border-top: 1px solid var(--card-white);
    border-bottom: 1px solid var(--card-white);
    font-size: 9.5px;
    font-weight: 300;
    letter-spacing: 0.1px;
    white-space: nowrap;
  }
</style>
</head>
<body>
<main class="canvas">
  <section class="card card--front" aria-label="Business card front">
    <svg class="front-corner" width="130" height="95" viewBox="0 0 130 95" aria-hidden="true">
      <path d="M0 0 H118 Q80 14 61 44 L30 50 L0 87 Z" fill="var(--brand-blue)"/>
    </svg>
    <div class="company-lockup">
      <p class="company-name">TOLMEN REFACING, LLC</p>
      <p class="company-tagline">Cabinets and Countertops</p>
    </div>
    <div class="person">
      <p class="person-name"><strong>Dorian</strong> Tolmen</p>
      <p class="person-role">Owner / Sales</p>
      <ul class="contact-list">
        <li class="contact-item">
          <svg class="contact-icon" width="11" height="11" viewBox="0 0 12 12" aria-hidden="true">
            <circle cx="6" cy="6" r="6" fill="var(--brand-blue)"/>
            <path d="M4 3 L5.2 4.6 L4.6 5.3 Q5.4 6.8 6.8 7.5 L7.5 6.9 L9 8 L8.3 9 Q5.5 9 3.2 4 Z" fill="#fff"/>
          </svg>
          <span>360-555-0147</span>
        </li>
        <li class="contact-item">
          <svg class="contact-icon" width="11" height="11" viewBox="0 0 12 12" aria-hidden="true">
            <circle cx="6" cy="6" r="6" fill="var(--brand-blue)"/>
            <rect x="3" y="4" width="6" height="4.2" fill="none" stroke="#fff" stroke-width="0.9"/>
            <path d="M3 4 L6 6.4 L9 4" fill="none" stroke="#fff" stroke-width="0.9"/>
          </svg>
          <span>dorian.tolmen@quenmail.com</span>
        </li>
      </ul>
    </div>
  </section>

  <section class="card card--back" aria-label="Business card back">
    <div class="back-lockup">
      <p class="back-name">TOLMEN REFACING LLC</p>
      <p class="back-tagline">CABINET REFACING AND COUNTERTOPS</p>
    </div>
  </section>
</main>
</body>
</html>
```